Need social media banner for ViewNest / Chirpel / Streamo / Mepline+

Hey all I have a channel called BrinkoTV it is a multi gaming channel but mostly consists of ZRK VT, GORB and Ironmoss Outrider when its released - Link is here - [url removed, login to view] As you can see I already am rocking an amazing Graphic Logo created by Pelkworks. However I would like a banner to match my logo for ViewNest, Chirpel, Mepline+ and Streamo ( these are all completely different sizes )

I would like the banner to match my logo if you go on my ViewNest channel you will see how it needs to be, same with chirpel - [url removed, login to view]
Can you make it a dark themed banner please? I will guarantee money also can it be done today please so its ready asap for when I am home..

Any other information please ask, here is my current logo. I am currently at work at the moment so cant send PSD however its just that file without the black around it. The banner does not have to have the logo in it, but on ViewNest the logo actually goes over the banner on the top left it you look.

Enjoy looking forward to doing business with you. I also would 100% need the banner to have my social media links on it, so a chirpel icon then /BirnkoTV streamo icon with /BrinkoTV palwall /BrinkoTV ViewNest /BrinkoTV if possible.

```html
<!DOCTYPE html>
<html lang="en">
<head>
<meta charset="utf-8">
<title>BrinkoTV – Channel Banner</title>
<link href="https://fonts.googleapis.com/css2?family=Russo+One&family=Oswald:wght@400&family=Cormorant+Garamond:wght@600&display=swap" rel="stylesheet">
<style>
  :root {
    --bg-deep: #04140f;
    --bg-mid: #0b3a26;
    --bg-glow: #116a45;
    --panel-dark: rgba(2, 14, 14, 0.55);
    --panel-teal: #0f4a4a;
    --panel-teal-edge: #17625f;
    --text-light: #eef3ef;
    --text-soft: #c9d3cf;
  }
  html, body {
    margin: 0;
    padding: 0;
    overflow: hidden;
    background: var(--bg-deep);
  }
  .banner {
    position: relative;
    width: 1200px;
    height: 207px;
    overflow: hidden;
  }
  .banner__texture {
    position: absolute;
    inset: 0;
    background:
      radial-gradient(ellipse 38% 70% at 52% 48%, var(--bg-glow) 0%, rgba(17,106,69,0) 100%),
      radial-gradient(ellipse 70% 110% at 50% 50%, var(--bg-mid) 0%, var(--bg-deep) 100%);
  }
  .banner__panels {
    position: absolute;
    inset: 0;
  }
  .banner__tagline {
    position: absolute;
    top: 17px;
    left: 0;
    width: 100%;
    text-align: center;
    font-family: "Oswald", sans-serif;
    font-size: 25px;
    letter-spacing: 0.5px;
    color: var(--text-light);
    margin: 0;
  }
  .banner__name {
    position: absolute;
    left: 0;
    top: 60px;
    width: 1200px;
    height: 90px;
  }
  .banner__name text {
    font-family: "Russo One", sans-serif;
    font-size: 96px;
    fill: var(--text-light);
  }
  .banner__socials {
    position: absolute;
    top: 162px;
    left: 0;
    width: 100%;
    display: flex;
    justify-content: center;
    align-items: center;
    gap: 16px;
    font-family: "Cormorant Garamond", serif;
    font-weight: 600;
    font-size: 20px;
    color: var(--text-soft);
    margin: 0;
    padding: 0;
    list-style: none;
  }
</style>
</head>
<body>
  <div class="banner">
    <div class="banner__texture" role="img" aria-label="Dark green grunge texture with scattered glowing particles"></div>

    <svg class="banner__panels" width="1200" height="207" viewBox="0 0 1200 207" aria-hidden="true">
      <polygon class="panel panel--left" points="0,0 290,0 220,207 0,207" fill="var(--panel-dark)"/>
      <polygon class="panel panel--right" points="1024,0 1200,0 1200,207 907,207" fill="var(--panel-teal)"/>
      <line class="panel__edge" x1="1024" y1="0" x2="907" y2="207" stroke="var(--panel-teal-edge)" stroke-width="2"/>
    </svg>

    <p class="banner__tagline">Official Channel of</p>

    <svg class="banner__name" viewBox="0 0 1200 90" aria-label="BrinkoTV">
      <text x="328" y="82" textLength="545" lengthAdjust="spacingAndGlyphs">BRINKOTV</text>
    </svg>

    <ul class="banner__socials">
      <li>Chirpel</li>
      <li>palwall</li>
      <li>Streamo</li>
      <li>Mepline+</li>
      <li>/BrinkoTV</li>
    </ul>
  </div>
</body>
</html>
```